Two Rollup Banners Promoting Trade Association

UPDATE: Please do not recycle the prior designs we've had. I am looking for creativity and a new look. Otherwise, I would use the prior designers to just update their work.
I need two 48"x79" Pull Up Retractable Banners Designed.
One promotes the benefits of membership in the Residential Capital Partners Forum. The second promotes RCPF's role in the affordable housing ecosystem.
The content for each is attached. I'm also providing examples of two banners we recently created for our 30th Anniversary as well as some photos of our members if you choose to use them (although it's not necessary - just providing them as an option).
The banners don't have to mimic the ones we did for our 30th Anniversary. I'm simply providing them as examples of designs that meet the look and feel of our brand.
I've also provided our brand guidelines and the specs for the banner.
Updates
All,
We are looking for clean, modern, streamlined designs. No clip art. No waves. Don’t bury the message in the graphics.
Please keep that in mind as you submit designs.
Look and feel
Each slider illustrates characteristics of the customer's brand and the style your logo design should communicate.

```html
<!DOCTYPE html>
<html lang="en">
<head>
<meta charset="utf-8">
<title>RCPF Rollup Banners</title>
<link href="https://fonts.googleapis.com/css2?family=Anton&family=Bebas+Neue&family=Montserrat:wght@500;600;700;800&display=swap" rel="stylesheet">
<style>
:root{
  --orange:#f04e23;
  --orange-deep:#c9401b;
  --slate:#5b656e;
  --slate-dark:#4a535b;
  --white:#ffffff;
  --stage:#f1f1f1;
}
*{margin:0;padding:0;box-sizing:border-box}
html,body{width:1200px;height:2161px;overflow:hidden}
body{background:var(--stage);position:relative;font-family:"Montserrat",sans-serif}
.banner{position:absolute;top:612px;width:570px;height:936px;overflow:hidden;background:var(--orange);box-shadow:0 10px 30px rgba(0,0,0,.18)}
.banner--membership{left:15px}
.banner--ecosystem{left:615px}

.photo-crowd{position:absolute;left:0;top:0;width:100%;height:380px;
  background:linear-gradient(180deg,#6e3219 0%,#8f3d1c 35%,#c24820 70%,var(--orange) 100%)}
.panel{position:absolute;left:0;top:0;width:100%;height:694px;border-radius:0 0 44px 44px;
  border-bottom:4px solid var(--white);background:linear-gradient(180deg,transparent 0,transparent 300px,var(--orange) 380px);z-index:2}
.photo-members{position:absolute;left:0;top:660px;width:100%;height:276px;z-index:1;
  background:linear-gradient(160deg,#5e5550 0%,#8a7c72 30%,#3c3a3d 55%,#9d8f86 80%,#6f6a6b 100%)}

.logo-tab{position:absolute;left:108px;top:0;width:354px;height:90px;background:var(--white);
  border-radius:0 0 44px 44px;display:flex;align-items:center;justify-content:center;gap:12px;z-index:3}
.logo-mark{width:34px;height:34px;background:var(--orange)}
.logo-name{font-family:"Montserrat",sans-serif;font-weight:800;color:var(--slate);display:flex;align-items:center;gap:10px}
.logo-name .acronym{font-size:40px;letter-spacing:-1px}
.logo-name .full{font-size:10px;line-height:1.15;width:140px;text-transform:uppercase}

.content{position:absolute;left:0;top:0;width:100%;z-index:3;text-align:center;color:var(--white)}
.headline{position:absolute;left:0;width:100%;font-family:"Anton",sans-serif;line-height:1;letter-spacing:-1px;text-transform:uppercase}
.headline--slate{color:var(--slate)}
.headline--orange{color:var(--orange)}
.outlined{text-shadow:
  3px 0 0 #fff,-3px 0 0 #fff,0 3px 0 #fff,0 -3px 0 #fff,
  2px 2px 0 #fff,-2px -2px 0 #fff,2px -2px 0 #fff,-2px 2px 0 #fff,
  4px 5px 6px rgba(0,0,0,.35)}
.rule{position:absolute;left:50%;transform:translateX(-50%);height:2px;
  background:linear-gradient(90deg,transparent,var(--white),transparent)}
.subhead{position:absolute;left:0;width:100%;font-family:"Bebas Neue",sans-serif;line-height:1}
.benefits{position:absolute;left:0;width:100%;list-style:none;font-size:15.5px;font-weight:500;line-height:26px}
.benefits b{font-weight:700}
.stats{position:absolute;left:0;width:100%;display:flex;justify-content:center;align-items:center;gap:12px}
.stat-num{font-family:"Bebas Neue",sans-serif;line-height:1}
.stat-label{text-align:left;font-size:15px;line-height:1.15;font-weight:500}
.footnote{position:absolute;left:0;width:100%;font-size:13px;font-weight:500}
.pillars{position:absolute;left:45px;right:20px;list-style:none;text-align:left;font-size:18.5px;font-weight:500;line-height:32px}
.pillars li::before{content:"•";margin-right:6px;font-size:12px;vertical-align:middle}

.cta-bar{position:absolute;left:56px;top:861px;width:460px;height:75px;z-index:4}
.cta-bar svg{position:absolute;inset:0}
.cta-text{position:absolute;inset:0;display:flex;align-items:center;justify-content:center;gap:26px;
  font-family:"Bebas Neue",sans-serif;font-size:40px;color:var(--white);padding-top:6px}
</style>
</head>
<body>

<section class="banner banner--membership">
  <div class="photo-crowd" role="img" aria-label="Members seated at a conference, tinted orange"></div>
  <div class="photo-members" role="img" aria-label="Investors in conversation at a roundtable session"></div>
  <div class="panel"></div>
  <div class="logo-tab">
    <span class="logo-mark"></span>
    <span class="logo-name"><span class="acronym">RCPF</span><span class="full">Residential Capital Partners Forum</span></span>
  </div>
  <div class="content">
    <h1 class="headline headline--slate outlined" style="top:140px;font-size:78px">LIHTC Investor</h1>
    <h1 class="headline headline--orange outlined" style="top:218px;font-size:78px">Only Community</h1>
    <div class="rule" style="top:313px;width:270px"></div>
    <h2 class="subhead" style="top:328px;font-size:50px">Where Investors</h2>
    <ul class="benefits" style="top:383px">
      <li><b>Network:</b> Peer Groups &amp; Forums</li>
      <li><b>Learn:</b> Conferences &amp; Webinars</li>
      <li><b>Share:</b> Candid Investor-Only Exchange</li>
      <li><b>Shape:</b> Industry Standards &amp; Best Practices</li>
      <li><b>Grow:</b> Professional Development &amp; Emerging Leaders Program</li>
    </ul>
    <h2 class="subhead" style="top:535px;font-size:38px">Our Community</h2>
    <div class="stats" style="top:572px">
      <span class="stat-num" style="font-size:66px">60+</span>
      <span class="stat-label">Investor<br>Firms</span>
      <span class="stat-num" style="font-size:66px;margin-left:8px">1,000+</span>
      <span class="stat-label">Industry<br>Professionals</span>
    </div>
    <p class="footnote" style="top:647px">Banks (Large &amp; Small), Insurance Companies, Economic Investors</p>
    <div class="rule" style="top:672px;width:270px;height:1px"></div>
  </div>
  <div class="cta-bar">
    <svg viewBox="0 0 460 75" preserveAspectRatio="none"><path d="M40 0 H430 L460 75 H0 C0 40 15 0 40 0 Z" fill="var(--slate)"/></svg>
    <div class="cta-text"><span>Join Us Today</span><span>www.rcpf.org</span></div>
  </div>
</section>

<section class="banner banner--ecosystem">
  <div class="photo-crowd" role="img" aria-label="Members listening during a conference session, tinted orange"></div>
  <div class="photo-members" role="img" aria-label="Two members in animated discussion at a conference"></div>
  <div class="panel"></div>
  <div class="logo-tab">
    <span class="logo-mark"></span>
    <span class="logo-name"><span class="acronym">RCPF</span><span class="full">Residential Capital Partners Forum</span></span>
  </div>
  <div class="content">
    <h1 class="headline headline--slate outlined" style="top:208px;font-size:64px">Where LIHTC Investing</h1>
    <h1 class="headline headline--orange outlined" style="top:276px;font-size:72px">Excellence Begins</h1>
    <div class="rule" style="top:362px;width:270px"></div>
    <ul class="pillars" style="top:384px">
      <li>Setting Industry Standards &amp; Best Practices</li>
      <li>Building Community Through Candid Exchange</li>
      <li>Promoting the Investor Perspective</li>
      <li>Fostering Collaboration Across the Ecosystem</li>
    </ul>
    <h2 class="subhead" style="top:528px;font-size:66px">30 Years of Impact</h2>
    <p class="footnote" style="top:598px;font-size:10.5px;font-weight:600">Industry-Adopted Standards in Underwriting, Asset Management, Risk Rating &amp; More</p>
    <div class="stats" style="top:622px;gap:8px">
      <span class="stat-num" style="font-size:44px">4 Million</span>
      <span class="stat-label" style="font-size:10.5px">Rental<br>Homes<br>Created</span>
      <span class="stat-num" style="font-size:44px;margin-left:10px">9.28 Million</span>
      <span class="stat-label" style="font-size:10.5px">Low-Income<br>Households Served</span>
    </div>
  </div>
  <div class="cta-bar">
    <svg viewBox="0 0 460 75" preserveAspectRatio="none"><path d="M40 0 H430 L460 75 H0 C0 40 15 0 40 0 Z" fill="var(--slate)"/></svg>
    <div class="cta-text"><span>Join Us Today</span><span>www.rcpf.org</span></div>
  </div>
</section>

</body>
</html>
```